Landing Page / Waitlist

I would like a landing page for people to sign up for a waiting list. The text on the page should include (but is not limited to):
1) Main point: The accounting system you'll love
2) Secondary points:
a. Ruthlessly efficient
b. Quietly intelligent
c. Driven by AI
I've attached a file of our logo

The design should be simple, clean, and innovative - this is an ai company

```html
<!DOCTYPE html>
<html lang="en">
<head>
<meta charset="utf-8">
<title>Ledgerlyn — Join the Waitlist</title>
<link rel="stylesheet" href="https://fonts.googleapis.com/css2?family=Inter:wght@400;500;600&display=swap">
<style>
  :root {
    --navy: #01062e;
    --royal: #0046bf;
    --azure: #0093ff;
    --sky: #00b8ff;
    --paper: #f7f8f9;
    --ice: #c4ecf8;
    --text-soft: rgba(247, 248, 249, 0.88);
    --footer-text: #3d5a78;
  }
  * { box-sizing: border-box; margin: 0; padding: 0; }
  html, body {
    width: 925px;
    height: 1200px;
    overflow: hidden;
    font-family: "Inter", Arial, sans-serif;
    background: var(--navy);
  }
  .landing {
    position: relative;
    width: 925px;
    height: 1200px;
    overflow: hidden;
    color: var(--paper);
    background:
      radial-gradient(ellipse 520px 260px at 24% 68%, rgba(196, 236, 248, 0.85), rgba(196, 236, 248, 0) 70%),
      linear-gradient(122deg,
        #1f7fc4 0%,
        #62bfe6 16%,
        var(--ice) 34%,
        #8fd3ef 44%,
        #1c6fb8 52%,
        #053f8f 62%,
        #0a5aa6 72%,
        #04316f 84%,
        var(--navy) 100%);
  }
  .landing::after {
    content: "";
    position: absolute;
    inset: 0;
    background: linear-gradient(180deg, rgba(1, 6, 46, 0) 70%, rgba(1, 40, 110, 0.35) 100%);
    pointer-events: none;
  }
  .grid-lines {
    position: absolute;
    inset: 0;
    width: 100%;
    height: 100%;
    opacity: 0.12;
  }
  .site-header {
    position: relative;
    z-index: 1;
    display: flex;
    justify-content: center;
    padding-top: 52px;
  }
  .brand {
    display: flex;
    align-items: center;
    gap: 7px;
    font-size: 17px;
    font-weight: 600;
    color: var(--paper);
    letter-spacing: -0.01em;
  }
  .brand-dot {
    width: 12px;
    height: 12px;
    border-radius: 50%;
    background: var(--sky);
  }
  .hero {
    position: relative;
    z-index: 1;
    text-align: center;
    margin-top: 300px;
  }
  .hero-title {
    font-size: 58px;
    font-weight: 600;
    line-height: 1.1;
    letter-spacing: -0.015em;
  }
  .hero-lead {
    margin-top: 22px;
    font-size: 15px;
    font-weight: 400;
    color: var(--text-soft);
  }
  .feature-list {
    list-style: none;
    display: flex;
    justify-content: center;
    gap: 42px;
    margin-top: 30px;
    font-size: 14px;
    font-weight: 500;
  }
  .feature-list li {
    display: flex;
    align-items: center;
    gap: 6px;
  }
  .feature-list svg { width: 12px; height: 12px; }
  .waitlist-form {
    display: flex;
    align-items: center;
    justify-content: space-between;
    width: 470px;
    height: 50px;
    margin: 36px auto 0;
    padding: 0 8px 0 22px;
    background: var(--paper);
    border-radius: 25px;
  }
  .waitlist-input {
    flex: 1;
    border: none;
    background: transparent;
    font-family: "Inter", Arial, sans-serif;
    font-size: 12px;
    color: var(--navy);
    outline: none;
  }
  .waitlist-input::placeholder { color: #6b7280; }
  .waitlist-button {
    display: flex;
    align-items: center;
    gap: 8px;
    height: 35px;
    padding: 0 16px;
    border: none;
    border-radius: 18px;
    background: var(--azure);
    color: var(--paper);
    font-family: "Inter", Arial, sans-serif;
    font-size: 12px;
    font-weight: 600;
  }
  .waitlist-button svg { width: 12px; height: 12px; }
  .site-footer {
    position: absolute;
    z-index: 1;
    left: 0;
    right: 0;
    bottom: 40px;
    text-align: center;
    font-size: 10px;
    color: var(--footer-text);
  }
</style>
</head>
<body>
  <main class="landing">
    <svg class="grid-lines" viewBox="0 0 925 1200" preserveAspectRatio="none" aria-hidden="true">
      <g stroke="#ffffff" stroke-width="1">
        <line x1="170" y1="0" x2="170" y2="1200"/>
        <line x1="330" y1="0" x2="330" y2="1200"/>
        <line x1="500" y1="0" x2="500" y2="1200"/>
        <line x1="640" y1="0" x2="640" y2="1200"/>
        <line x1="780" y1="0" x2="780" y2="1200"/>
        <line x1="0" y1="110" x2="925" y2="110"/>
        <line x1="0" y1="290" x2="925" y2="290"/>
        <line x1="0" y1="470" x2="925" y2="470"/>
      </g>
    </svg>

    <header class="site-header">
      <div class="brand"><span class="brand-dot"></span>Ledgerlyn</div>
    </header>

    <section class="hero">
      <h1 class="hero-title">The accounting system<br>you will love</h1>
      <p class="hero-lead">Let AI reconcile, predict, and optimize - so you never touch a spreadsheet again.</p>

      <ul class="feature-list">
        <li>
          <svg viewBox="0 0 12 12" aria-hidden="true"><path d="M2 6.5 L4.8 9.2 L10 3" fill="none" stroke="#00b8ff" stroke-width="1.6" stroke-linecap="round" stroke-linejoin="round"/></svg>
          Ruthlessly efficient
        </li>
        <li>
          <svg viewBox="0 0 12 12" aria-hidden="true"><path d="M2 6.5 L4.8 9.2 L10 3" fill="none" stroke="#00b8ff" stroke-width="1.6" stroke-linecap="round" stroke-linejoin="round"/></svg>
          Quietly intelligent
        </li>
        <li>
          <svg viewBox="0 0 12 12" aria-hidden="true"><path d="M2 6.5 L4.8 9.2 L10 3" fill="none" stroke="#f7f8f9" stroke-width="1.6" stroke-linecap="round" stroke-linejoin="round"/></svg>
          Driven by AI
        </li>
      </ul>

      <form class="waitlist-form">
        <input class="waitlist-input" type="email" placeholder="Enter your email address" aria-label="Email address">
        <button class="waitlist-button" type="button">
          Join the Waitlist
          <svg viewBox="0 0 12 12" aria-hidden="true"><path d="M1.5 6 H10 M6.8 2.8 L10 6 L6.8 9.2" fill="none" stroke="#f7f8f9" stroke-width="1.4" stroke-linecap="round" stroke-linejoin="round"/></svg>
        </button>
      </form>
    </section>

    <footer class="site-footer">Ledgerlyn © 2025 All Rights Reserved</footer>
  </main>
</body>
</html>
```